Web design for cloud computing startup

Our company is called BrightLedgerHub and we are a cloud computing startup that automates the purchasing to payment process for any company. This is a B2B solution targeting small and medium enterprises across different industries. Our application allows buyers to create electronic purchase orders and send them to suppliers. In turn, suppliers can generate invoices based on purchase orders. In addition to organizing and formalizing interactions between buyers and suppliers our system is environment friendly as it significantly reduces the amount of paper buyers and suppliers use.

Our mission is to become the leader on the market of cloud based software for procurement by delivering easy-integrated and cost effective solutions to help our customers improve operational efficiency and boost profitability of business.

We need your help to design 2 pages:
- Homepage
- Content page

Please use 3 colors for the webpages: white, blue, and green. White and blue should be primary colors, while green should just emphasize that we are environment friendly solution.

The words we are using to describe the website are the following:
- Simple and minimalist
- Modern, clean and light
- Professional and reliable
- Creative (we want something different from standard website template)
- Calling to action

Please see attached design examples for homepage and content page that we like (please note that attached examples are only for the page structures not for the color schemes).

In addition to features mentioned in the attached ppt, homepage should have:
- Rotating banner with 3 different pictures (one of them featuring environmental aspect of our solution)
- Contact us on Pagewall, Quello, Tramvoy

Reason: I've updated the project brief, eliminating some of the requirements giving you more freedom.

Reason: Requests from designers to extend deadline

Target Market(s)

Small and Medium Enterprises. Primary users of the website are senior executives of those companies so website needs to account for this.

Industry/Entity Type

Environment

Requirements
Must have
• - For the final design we need PSD files with all the original layers
- The width needs to be a size that will work with every size computer screen
- Need to use cross-platform compatible font

Please feel free to ask any questions to help you refine your design.
Look forward to seeing your designs. Thank you all for your time and efforts.

```html
<!DOCTYPE html>
<html lang="en">
<head>
<meta charset="utf-8">
<title>BrightLedgerHub</title>
<link rel="stylesheet" href="https://fonts.googleapis.com/css2?family=Source+Sans+3:wght@400;600&display=swap">
<style>
:root{
  --page:#f3f7fb;
  --header-top:#ffffff;
  --header-bottom:#e8f0f8;
  --header-line:#d3e0ee;
  --panel:#ffffff;
  --panel-line:#d6e2ee;
  --brand-blue:#1f6fb8;
  --accent-blue:#2b8fd6;
  --accent-green:#5aa832;
  --nav-text:#4b5d70;
  --nav-active:#1f6fb8;
  --body-text:#3d4b59;
  --footer-text:#7d8c9a;
  --field:#ffffff;
  --field-line:#b9cadb;
  --dropdown:rgba(31,111,184,.92);
  --hero-blue:#3f8fd8;
  --hero-light:#cfe6f7;
  --hero-green:#8cc63f;
  --video:#17324f;
}
*{box-sizing:border-box;margin:0;padding:0}
html,body{width:1200px;height:955px;overflow:hidden}
body{background:var(--page);font-family:"Source Sans 3",Arial,sans-serif;position:relative;color:var(--body-text)}
.site-header{position:absolute;left:0;top:0;width:1200px;height:138px;background:linear-gradient(var(--header-top),var(--header-bottom));border-bottom:1px solid var(--header-line)}
.brand{position:absolute;left:53px;top:86px;font-size:29px;font-weight:600;color:var(--brand-blue);letter-spacing:.3px}
.help-line{position:absolute;left:716px;top:38px;font-size:13px;color:var(--accent-blue)}
.help-line b{font-weight:600}
.help-line .tel{font-size:16px}
.search{position:absolute;left:913px;top:28px;width:228px;height:31px;background:#fff;border:1px solid var(--field-line)}
.search svg{position:absolute;right:12px;top:6px}
.main-nav{position:absolute;top:90px;left:449px;height:34px;display:flex;font-size:14.5px}
.main-nav a{display:block;padding:9px 11px 0;color:var(--nav-text);text-decoration:none;height:34px;text-transform:uppercase}
.main-nav a.current{color:var(--nav-active);font-weight:600}
.main-nav a.open{background:#fff;border:1px solid var(--header-line);border-bottom:none;color:var(--nav-active)}
.banner{position:absolute;left:0;top:138px;width:1200px;height:391px;background:#e4edf6}
.banner-photo{position:absolute;left:34px;top:0;width:1130px;height:391px;background:linear-gradient(160deg,var(--hero-blue) 0%,var(--hero-light) 60%,var(--hero-green) 100%)}
.banner-arrow{position:absolute}
.dropdown{position:absolute;left:506px;top:124px;width:242px;height:208px;background:var(--dropdown);list-style:none;padding:14px 0 0 21px}
.dropdown li{font-size:13.5px;color:#fff;height:34px;display:flex;align-items:center;text-transform:uppercase}
.dropdown li::before{content:"";width:7px;height:7px;border:1.5px solid #fff;border-radius:50%;margin-right:6px}
.content-panel{position:absolute;left:34px;top:539px;width:1130px;height:326px;background:var(--panel);border:1px solid var(--panel-line)}
.video{position:absolute;left:46px;top:555px;width:362px;height:276px;background:var(--video);border:1px solid var(--panel-line)}
.video .reel{position:absolute;left:136px;top:88px}
.video-controls{position:absolute;left:0;bottom:0;width:100%;height:30px;background:linear-gradient(#2c4a6a,#10253c);border-top:1px solid #3f6285}
.video-controls svg{position:absolute;left:0;top:0}
.video-controls .time{position:absolute;right:40px;top:9px;font-size:8px;color:#b8cbe0}
.section-title{font-size:21px;font-weight:600;color:var(--brand-blue)}
.why{position:absolute;left:469px;top:555px;width:346px}
.why .section-title{position:absolute;left:45px;top:12px}
.why .doc{position:absolute;left:3px;top:0}
.why p{font-size:13.5px;line-height:17px;text-align:justify;color:var(--body-text)}
.why .p1{position:absolute;top:52px;width:346px}
.why .p2{position:absolute;top:153px;width:346px}
.login{position:absolute;left:879px;top:566px;width:225px}
.login .section-title{position:absolute;left:28px;top:0}
.login .key{position:absolute;left:0;top:3px}
.login .field{position:absolute;left:0;width:225px;height:35px;background:var(--field);border:1px solid var(--field-line)}
.social{position:absolute;right:53px;top:826px;display:flex;gap:12px;font-size:12.5px;font-weight:600;color:var(--brand-blue)}
.footer-nav{position:absolute;top:885px;left:0;width:1200px;text-align:center;font-size:12.5px;color:var(--footer-text)}
.footer-nav span{margin:0 4px}
</style>
</head>
<body>
<header class="site-header">
  <div class="brand">BrightLedgerHub</div>
  <div class="help-line">need help? <b>TEL:</b> <span class="tel">555.204.3170</span></div>
  <div class="search">
    <svg width="22" height="18" viewBox="0 0 22 18"><circle cx="7" cy="7" r="5" fill="none" stroke="#6d8299" stroke-width="2"/><line x1="11" y1="10" x2="19" y2="16" stroke="#6d8299" stroke-width="2.5"/></svg>
  </div>
  <nav class="main-nav">
    <a class="current">Home</a>
    <a class="open">Company</a>
    <a>Solutions</a>
    <a>How to save</a>
    <a>Save the Earth</a>
    <a>Knowledge center</a>
    <a>Contact us</a>
  </nav>
</header>

<section class="banner">
  <div class="banner-photo" role="img" aria-label="Rotating banner photo about paper-free, environment friendly procurement"></div>
  <svg class="banner-arrow" style="left:47px;top:171px" width="50" height="50" viewBox="0 0 50 50"><circle cx="25" cy="25" r="23" fill="none" stroke="#ffffff" stroke-width="2.5" opacity=".85"/><path d="M31 13 L14 25 L31 37 L26 25 Z" fill="#ffffff" opacity=".9"/></svg>
  <svg class="banner-arrow" style="left:1092px;top:171px" width="50" height="50" viewBox="0 0 50 50"><circle cx="25" cy="25" r="23" fill="none" stroke="#fff" stroke-width="2.5"/><path d="M19 13 L36 25 L19 37 L24 25 Z" fill="#fff"/></svg>
</section>

<ul class="dropdown">
  <li>About BLH</li>
  <li>&nbsp;Why BLH</li>
  <li>Customer testimonials</li>
  <li>Our management</li>
  <li>Careers</li>
</ul>

<div class="content-panel"></div>

<div class="video">
  <svg class="reel" width="100" height="72" viewBox="0 0 100 72"><circle cx="33" cy="34" r="31" fill="none" stroke="#9fbbd8" stroke-width="3"/><circle cx="33" cy="18" r="8" fill="#9fbbd8"/><circle cx="33" cy="50" r="8" fill="#9fbbd8"/><circle cx="17" cy="34" r="8" fill="#9fbbd8"/><circle cx="49" cy="34" r="8" fill="#9fbbd8"/><circle cx="33" cy="34" r="3" fill="#9fbbd8"/><path d="M52 60 Q68 74 76 60 Q82 56 96 70" fill="none" stroke="#9fbbd8" stroke-width="3"/></svg>
  <div class="video-controls">
    <svg width="362" height="30" viewBox="0 0 362 30"><circle cx="15" cy="14" r="7" fill="#4d6f93"/><path d="M13 11 L18 14 L13 17Z" fill="#fff"/><circle cx="32" cy="14" r="7" fill="#4d6f93"/><rect x="29.5" y="11.5" width="5" height="5" fill="#fff"/><rect x="46" y="8" width="225" height="12" rx="6" fill="#0c1d30"/><rect x="46" y="8" width="115" height="12" rx="6" fill="#5aa832"/><circle cx="122" cy="14" r="4" fill="#e8f3dc"/><circle cx="332" cy="14" r="7" fill="#4d6f93"/><circle cx="349" cy="14" r="7" fill="#4d6f93"/></svg>
    <span class="time">- 00:02:23</span>
  </div>
</div>

<section class="why">
  <svg class="doc" width="33" height="40" viewBox="0 0 33 40"><path d="M2 2 H24 L31 9 V38 H2 Z" fill="#eef4fa" stroke="#b9cadb"/><path d="M24 2 V9 H31" fill="#cfdceb"/><path d="M9 27 H24 A4 4 0 0 0 23 19 A6 6 0 0 0 12 19 A4 4 0 0 0 9 27 Z" fill="none" stroke="#5aa832" stroke-width="2"/></svg>
  <h2 class="section-title">Why BLH?</h2>
  <p class="p1">We are a cloud procurement platform that turns purchase orders and invoices into simple online steps for small and medium businesses in every industry.</p>
  <p class="p2">Buyers send electronic orders and suppliers answer with invoices in one click - less paper, fewer errors and faster payment. Our team shares one goal: efficient, greener business.</p>
</section>

<section class="login">
  <svg class="key" width="22" height="22" viewBox="0 0 22 22"><circle cx="11" cy="11" r="10" fill="#5aa832"/><circle cx="11" cy="9" r="3" fill="#fff"/><rect x="10" y="10" width="2" height="6" fill="#fff"/></svg>
  <h2 class="section-title">Client Login</h2>
  <div class="field" style="top:47px"></div>
  <div class="field" style="top:94px"></div>
  <svg style="position:absolute;left:184px;top:145px" width="40" height="32" viewBox="0 0 40 32"><path d="M24 6 A13 13 0 1 0 24 26" fill="none" stroke="#2b8fd6" stroke-width="5"/><path d="M16 16 H34 M28 10 L35 16 L28 22" fill="none" stroke="#2b8fd6" stroke-width="4"/></svg>
</section>

<div class="social">
  <span>Searchly</span><span>Quello</span><span>Tramvoy</span><span>Pagewall</span>
</div>

<nav class="footer-nav">
  Home <span>|</span> Company <span>|</span> Solutions <span>|</span> How to save <span>|</span> Save the Earth <span>|</span> Knowledge center <span>|</span> Contact us
</nav>
</body>
</html>
```